Corvalen Capital Modern Business Card

We need a modern business card template designed for Corvalen Capital.
Corvalen Capital is a diversified global cryptocurrency investment fund.

The font under the logo: Hiragino Kaku Gothic Pro

Color Hexcode: Main colors white (ffffff) & teal (188383), we are open to adding #fcca46 as an accent

Need time to get feedback from my team and to make sure designers better understand the brief.

Target Market(s)

Accredited Investors, high net worth individuals and institutional investors

Industry/Entity Type

Investment

Contact Information for Business Card

Contact Information should contain
Name
main phone +1 720 555 0147
cell
email

Font styles to use
Sans Serif
Other font styles liked:
• Hiragino Kaku Gothic Pro

Requirements
Must have
• would like to have icons that identify the contact information
• include our website: www.corvalencapital.example
• include our Tagline: Diversified Crypto Investment Funds
Nice to have
• Would like to have a simple back side with the logo (without the words) and plenty of space

```html
<!DOCTYPE html>
<html lang="en">
<head>
<meta charset="utf-8">
<title>Corvalen Capital – Business Card</title>
<link rel="stylesheet" href="https://fonts.googleapis.com/css2?family=Arimo:wght@400;700&family=Noto+Sans+JP:wght@400;500&display=swap">
<style>
  :root {
    --teal: #188383;
    --teal-mid: #23979a;
    --ink: #1d1d1f;
    --paper: #ffffff;
    --stage: #25262b;
  }
  * { box-sizing: border-box; margin: 0; padding: 0; }
  html, body {
    width: 1200px; height: 960px; overflow: hidden;
    background: var(--stage);
  }
  .stage { position: relative; width: 1200px; height: 960px; }

  .card {
    position: absolute;
    width: 700px; height: 400px;
    background: var(--paper);
    box-shadow: 0 14px 30px rgba(0,0,0,.45);
    overflow: hidden;
  }
  .card--front { left: 110px; top: 60px; }
  .card--contact { left: 390px; top: 500px; }

  /* Front: brand name + tagline */
  .brand-block {
    position: absolute; inset: 0;
    display: flex; flex-direction: column;
    align-items: center; justify-content: center;
    gap: 22px;
  }
  .brand-name {
    display: flex; align-items: center; gap: 16px;
    font-family: "Noto Sans JP", "Arimo", sans-serif;
    font-weight: 500;
    font-size: 44px;
    letter-spacing: 3px;
    text-transform: uppercase;
    color: var(--teal-mid);
  }
  .brand-mark { width: 26px; height: 26px; background: var(--teal-mid); flex: none; }
  .tagline {
    font-family: "Arimo", sans-serif;
    font-size: 19px;
    letter-spacing: 1.5px;
    text-transform: uppercase;
    color: var(--teal-mid);
  }

  /* Contact side */
  .corner-brand {
    position: absolute; top: 46px; right: 48px;
    display: flex; align-items: center; gap: 10px;
    font-family: "Noto Sans JP", "Arimo", sans-serif;
    font-size: 17px; letter-spacing: 1px;
    text-transform: uppercase;
    color: var(--ink);
  }
  .corner-brand .brand-mark { width: 14px; height: 14px; }

  .person { position: absolute; left: 56px; top: 150px; }
  .person-name {
    font-family: "Arimo", sans-serif;
    font-size: 30px; letter-spacing: 1px;
    text-transform: uppercase;
    color: var(--teal-mid);
    line-height: 1.1;
  }
  .person-role {
    font-family: "Arimo", sans-serif;
    font-size: 19px; color: var(--ink);
    margin: 4px 0 0 14px;
  }

  .contact-list {
    list-style: none;
    position: absolute; left: 70px; top: 246px;
    display: flex; flex-direction: column; gap: 10px;
  }
  .contact-item {
    display: flex; align-items: center; gap: 14px;
    font-family: "Arimo", sans-serif;
    font-size: 19px; color: var(--ink);
  }
  .contact-icon { width: 20px; height: 20px; flex: none; }
</style>
</head>
<body>
<main class="stage">

  <section class="card card--front" aria-label="Card front">
    <div class="brand-block">
      <div class="brand-name"><span class="brand-mark"></span>Corvalen Capital</div>
      <p class="tagline">Diversified Crypto Investment Funds</p>
    </div>
  </section>

  <section class="card card--contact" aria-label="Card contact side">
    <div class="corner-brand"><span class="brand-mark"></span>Corvalen Capital</div>

    <div class="person">
      <h1 class="person-name">Jonathane Doe</h1>
      <p class="person-role">CEO</p>
    </div>

    <ul class="contact-list">
      <li class="contact-item">
        <svg class="contact-icon" viewBox="0 0 20 20" aria-hidden="true">
          <rect x="5" y="1.5" width="10" height="17" rx="1.8" fill="none" stroke="#188383" stroke-width="1.6"/>
          <line x1="8.5" y1="15.5" x2="11.5" y2="15.5" stroke="#188383" stroke-width="1.4"/>
        </svg>
        +1 720 555 0198
      </li>
      <li class="contact-item">
        <svg class="contact-icon" viewBox="0 0 20 20" aria-hidden="true">
          <path d="M5 3 L8 3 L9 7 L7 8.5 C8 11 9.5 12.5 12 13.5 L13.5 11.5 L17.5 12.5 L17.5 15.5 C17.5 16.5 16.5 17.5 15.5 17.5 C9 17 3 11 2.5 5 C2.5 4 3.5 3 5 3 Z" fill="#188383"/>
        </svg>
        +1 720 555 0147
      </li>
      <li class="contact-item">
        <svg class="contact-icon" viewBox="0 0 20 20" aria-hidden="true">
          <rect x="1.5" y="4" width="17" height="12" fill="none" stroke="#188383" stroke-width="1.6"/>
          <polyline points="1.5,4 10,11 18.5,4" fill="none" stroke="#188383" stroke-width="1.6"/>
        </svg>
        hello@corvalencapital.example
      </li>
      <li class="contact-item">
        <svg class="contact-icon" viewBox="0 0 20 20" aria-hidden="true">
          <circle cx="10" cy="10" r="8.5" fill="#188383"/>
          <ellipse cx="10" cy="10" rx="3.5" ry="8.5" fill="none" stroke="#fff" stroke-width="1.2"/>
          <line x1="1.5" y1="10" x2="18.5" y2="10" stroke="#fff" stroke-width="1.2"/>
        </svg>
        www.corvalencapital.example
      </li>
    </ul>
  </section>

</main>
</body>
</html>
```